Pinecrest Renovations - Get the creative juices going!!

Pinecrest does not do the actual renovation work. The company provides high end project management of renovation (primarily residential - with an eye toward commercial) The renovation work could look very different between projects. This company manages the work of contractors, architects and interior designers (either subcontracted directly by Pinecrest or hired by the client and entrusted to Pinecrest to manage). Clients are high end in the economic scale and the card needs to have a high end feel to it.

The owner is female, but the audience will be heavily slanted male. It should not be a "feminine" or "masculine" looking card. If anything, slant more on the masculine side. Clean, simple, yet creative and artistically appealing. The card design should complement and in no way compete with the logo.

When people think of our company: trust, integrity, dynamic, limitless possibilities, transition, energy, creative. We plan to expand in the future to be international.

There will also be a contest running for stationary. Please check that section, as well.

***Black is 80-90 percent black. Not stark black

Tight timeline. Needs cards printed quickly!

Residential

```html
<!DOCTYPE html>
<html lang="en">
<head>
<meta charset="utf-8">
<title>Pinecrest Renovations – Business Card</title>
<link rel="stylesheet" href="https://fonts.googleapis.com/css2?family=Questrial&family=Old+Standard+TT&display=swap">
<style>
  :root {
    --charcoal: #333333;
    --teal: #1aaba3;
    --white: #ffffff;
    --ink-grey: #4a4a4a;
  }
  html, body {
    margin: 0;
    padding: 0;
    width: 1200px;
    height: 685px;
    overflow: hidden;
    background: var(--charcoal);
  }
  .card {
    position: relative;
    width: 1200px;
    height: 685px;
    background: var(--charcoal);
  }
  .house-emblem {
    position: absolute;
    left: 0;
    top: 0;
    width: 720px;
    height: 610px;
  }
  .house-emblem .roof-body { fill: var(--teal); }
  .house-emblem .house-panel { fill: var(--white); }
  .brand-mark {
    position: absolute;
    left: 223px;
    top: 232px;
    width: 144px;
    height: 144px;
    background: var(--teal);
  }
  .brand-name {
    position: absolute;
    left: 68px;
    width: 454px;
    top: 440px;
    margin: 0;
    text-align: center;
    font-family: "Questrial", "Century Gothic", sans-serif;
    font-weight: 400;
    font-size: 33px;
    line-height: 40px;
    letter-spacing: 0.5px;
    color: var(--ink-grey);
    text-transform: uppercase;
    white-space: nowrap;
  }
  .contact-list {
    position: absolute;
    left: 742px;
    top: 127px;
    margin: 0;
    padding: 0;
    list-style: none;
    font-family: "Old Standard TT", "Century Schoolbook", serif;
    font-size: 45px;
    letter-spacing: 1.5px;
    color: var(--teal);
  }
  .contact-list li {
    height: 97.5px;
    line-height: 50px;
    white-space: nowrap;
  }
</style>
</head>
<body>
  <main class="card">
    <svg class="house-emblem" viewBox="0 0 720 610" aria-hidden="true">
      <path class="roof-body" d="M0,200 L278,81 Q290,75 302,81 L688,243 Q712,256 710,282 Q706,310 672,312 L590,312 L590,575 Q590,603 562,603 L0,603 Z"/>
      <path class="house-panel" d="M68,243 L291,147 L522,243 L522,535 L68,535 Z"/>
    </svg>
    <div class="brand-mark" aria-hidden="true"></div>
    <p class="brand-name">Pinecrest Renovations</p>
    <ul class="contact-list">
      <li>Adress :</li>
      <li>Tel&nbsp; :</li>
      <li>Fax :</li>
      <li>www.website.com</li>
      <li>email@email.com</li>
    </ul>
  </main>
</body>
</html>
```